Business Card Design

Attached is the logo of the store.

Information needed on the business card:

www.vault82vino.com
info@vault82vino.com
412 7th Ave NY, NY 10036
Tel:(646) 555-0147

Store Hours
Mon-Sat Noon-10pm
Sun Noon-8pm

Free Deliveries

Industry/Entity Type

Business

Contact Information for Business Card

Bramble 82 Wine & Spirits

```html
<!DOCTYPE html>
<html lang="en">
<head>
<meta charset="utf-8">
<title>Bramble 82 Wine &amp; Spirits – Business Card</title>
<link href="https://fonts.googleapis.com/css2?family=Questrial&display=swap" rel="stylesheet">
<style>
  :root {
    --page: #ffffff;
    --card-dark: #0b0b0c;
    --card-mid: #1c1d20;
    --silver-light: #f4f4f4;
    --silver-mid: #b9b9bb;
    --silver-dark: #7b7b7e;
    --text-light: #f2f2f2;
    --accent-red: #e0222b;
  }
  * { box-sizing: border-box; margin: 0; padding: 0; }
  html, body {
    width: 1200px;
    height: 900px;
    overflow: hidden;
    background: var(--page);
    font-family: "Questrial", "Century Gothic", sans-serif;
  }
  .sheet {
    position: relative;
    width: 1200px;
    height: 900px;
  }
  .card {
    position: absolute;
    top: 290px;
    width: 560px;
    height: 320px;
    overflow: hidden;
    background:
      radial-gradient(ellipse at 50% 40%, var(--card-mid) 0%, var(--card-dark) 75%);
    color: var(--text-light);
  }
  .card--front { left: 20px; }
  .card--back { left: 620px; }

  .brand-name {
    position: absolute;
    color: var(--silver-mid);
    font-size: 38px;
    font-weight: 400;
    letter-spacing: 1px;
    white-space: nowrap;
  }
  .card--front .brand-name {
    left: 0;
    right: 0;
    top: 78px;
    text-align: center;
  }
  .card--back .brand-name {
    left: 30px;
    top: 88px;
    width: 300px;
    font-size: 34px;
    line-height: 44px;
    white-space: normal;
  }
  .brand-name .line { display: block; }

  .silver-band {
    position: absolute;
    left: 0;
    right: 0;
    top: 183px;
    height: 12px;
    background: linear-gradient(180deg, var(--silver-light) 0%, var(--silver-mid) 50%, var(--silver-dark) 100%);
  }

  .contact-list {
    position: absolute;
    left: 30px;
    top: 208px;
    list-style: none;
    font-size: 18px;
    line-height: 23px;
  }
  .contact-list li {
    display: flex;
    align-items: center;
    gap: 6px;
  }
  .contact-icon {
    width: 18px;
    height: 18px;
    flex: none;
    fill: var(--accent-red);
  }

  .store-info {
    position: absolute;
    right: 28px;
    top: 208px;
    text-align: right;
    font-size: 15px;
    line-height: 20px;
  }
  .store-info .deliveries {
    margin-top: 18px;
    color: var(--accent-red);
  }

  .feature-art {
    position: absolute;
    right: 0;
    top: 0;
    width: 200px;
    height: 320px;
    background: linear-gradient(90deg, var(--silver-dark) 0%, var(--silver-light) 45%, var(--silver-mid) 100%);
  }
</style>
</head>
<body>
<main class="sheet">

  <section class="card card--front" aria-label="Business card front">
    <h1 class="brand-name">Bramble 82 Wine &amp; Spirits</h1>
    <div class="silver-band"></div>

    <ul class="contact-list">
      <li>
        <svg class="contact-icon" viewBox="0 0 24 24" aria-hidden="true"><path d="M6.6 10.8a15 15 0 0 0 6.6 6.6l2.2-2.2a1 1 0 0 1 1-.25 11.4 11.4 0 0 0 3.6.57 1 1 0 0 1 1 1V20a1 1 0 0 1-1 1A17 17 0 0 1 3 4a1 1 0 0 1 1-1h3.5a1 1 0 0 1 1 1c0 1.25.2 2.450.57 3.57a1 1 0 0 1-.25 1z"/></svg>
        (646) 555-0147
      </li>
      <li>
        <svg class="contact-icon" viewBox="0 0 24 24" aria-hidden="true"><path fill-rule="evenodd" d="M12 2a10 10 0 1 0 0 20 10 10 0 0 0 0-20zm-1 2.1V8H7.3A8 8 0 0 1 11 4.1zm2 0A8 8 0 0 1 16.7 8H13zM6.3 10H11v4H6.3a8 8 0 0 1 0-4zm6.7 0h4.7a8 8 0 0 1 0 4H13zm-5.7 6H11v3.9A8 8 0 0 1 7.3 16zm5.7 0h3.7A8 8 0 0 1 13 19.9z"/></svg>
        www.vault82vino.com
      </li>
      <li>
        <svg class="contact-icon" viewBox="0 0 24 24" aria-hidden="true"><path d="M3 5h18a1 1 0 0 1 1 1v1l-10 6L2 7V6a1 1 0 0 1 1-1zm-1 4.3 10 6 10-6V18a1 1 0 0 1-1 1H3a1 1 0 0 1-1-1z"/></svg>
        info@vault82vino.com
      </li>
      <li>
        <svg class="contact-icon" viewBox="0 0 24 24" aria-hidden="true"><path d="M12 3 2 12h3v9h5v-6h4v6h5v-9h3z"/></svg>
        412 7th Ave NY, NY 10036
      </li>
    </ul>

    <div class="store-info">
      <p>Store Hours</p>
      <p>Mon-Sat Noon-10pm</p>
      <p>Sun Noon-8pm</p>
      <p class="deliveries">Free Deliveries</p>
    </div>
  </section>

  <section class="card card--back" aria-label="Business card back">
    <h2 class="brand-name"><span class="line">Bramble 82</span><span class="line">Wine &amp; Spirits</span></h2>
    <div class="feature-art" role="img" aria-label="Silver silhouette of a woman sipping red wine from a glass"></div>
  </section>

</main>
</body>
</html>
```